ZENITH conference Slide Deck

This is a conference for our team that will be 3 days of discussions on how to build our business in the middle of these challenging time. Its a bit of a battle and so we are going with a red and grey/black these although I am open to your interpretation. I will include a few graphics that we have started on to show you the look. But I am just getting started, INSPIRE ME! The screen will be 100' across the front of the room and these decks will show on each side and I will reformat for the middle 1X6 screen as needed. I have the AI file of the logo if you need it. I don't see where to upload it here.

Target Market(s)

our top producers

Industry/Entity Type

Real Estate Agent

Font styles to use
Sans Serif

Colors
ec1f27

Requirements
Must have
• Depth, creativity

```html
<!DOCTYPE html>
<html lang="en">
<head>
<meta charset="utf-8">
<title>ZENITH Conference Slide</title>
<link rel="stylesheet" href="https://fonts.googleapis.com/css2?family=Montserrat:wght@400;700;800&display=swap">
<style>
  :root {
    --red: #ec1f27;
    --ink: #0b0b0b;
    --paper: #f4f4f4;
    --black: #000000;
    --white: #ffffff;
    --text: #1e1e1e;
  }
  * { margin: 0; padding: 0; box-sizing: border-box; }
  html, body { width: 1200px; height: 675px; overflow: hidden; background: var(--paper); }
  .slide {
    position: relative;
    width: 1200px;
    height: 675px;
    overflow: hidden;
    background: var(--paper);
    font-family: "Montserrat", sans-serif;
  }
  .slide-art { position: absolute; inset: 0; }
  .headline {
    position: absolute;
    left: 101px;
    top: 171.5px;
    font-weight: 800;
    font-size: 39px;
    line-height: 45px;
    letter-spacing: 0.12em;
    color: var(--ink);
    text-transform: uppercase;
  }
  .point-number {
    position: absolute;
    left: 101px;
    font-weight: 800;
    font-size: 37px;
    line-height: 1;
    color: var(--red);
  }
  .point-text {
    position: absolute;
    left: 173px;
    width: 380px;
    font-weight: 400;
    font-size: 22px;
    line-height: 24.3px;
    color: var(--text);
    letter-spacing: 0.01em;
  }
  .brand-name {
    font-family: "Montserrat", sans-serif;
    font-weight: 800;
    font-size: 42px;
    fill: var(--red);
    letter-spacing: 0.02em;
  }
  .caption-text {
    font-family: "Montserrat", sans-serif;
    font-weight: 700;
    font-size: 27px;
    fill: var(--white);
    letter-spacing: 0.08em;
  }
</style>
</head>
<body>
<main class="slide">
  <svg class="slide-art" width="1200" height="675" viewBox="0 0 1200 675" xmlns="http://www.w3.org/2000/svg">
    <defs>
      <linearGradient id="interior-tone" x1="0" y1="0" x2="0" y2="1">
        <stop offset="0" stop-color="#8fb4d6"/>
        <stop offset="0.45" stop-color="#b9d2e6"/>
        <stop offset="0.75" stop-color="#dde8f1"/>
        <stop offset="1" stop-color="#eef3f8"/>
      </linearGradient>
    </defs>

    <!-- dark backdrop panel -->
    <polygon class="backdrop-panel" points="914,0 1200,0 1200,675 856,675" fill="var(--black)"/>

    <!-- slanted accent band -->
    <polygon class="accent-band" points="692.6,174.7 723.4,174.7 681.5,675 649.8,675" fill="var(--red)"/>

    <!-- photo placeholder -->
    <polygon class="photo-area" role="img" aria-label="Photo of a bright modern glass-walled office interior with trees outside"
             points="723.4,174.7 1112.3,174.7 1112.3,675 681.5,675" fill="url(#interior-tone)"/>

    <!-- slanted outline frame -->
    <polygon class="feature-frame" points="846.4,50.3 1158,50.3 1158,581.8 800.7,581.8"
             fill="none" stroke="var(--red)" stroke-width="8.8" stroke-linejoin="miter"/>

    <!-- caption bar -->
    <rect class="caption-bar" x="842" y="504.5" width="320.7" height="54.5" fill="var(--red)"/>
    <text class="caption-text" x="1113" y="541.7" text-anchor="end">ADD CAPTION</text>

    <!-- event name -->
    <text class="brand-name" x="1111" y="131" text-anchor="end">ZENITH</text>

    <!-- headline bracket -->
    <polyline class="headline-bracket" points="192.4,157.5 76,157.5 76,282.7 184.5,282.7 187.5,266"
              fill="none" stroke="var(--red)" stroke-width="7.5" stroke-linejoin="miter"/>
  </svg>

  <h1 class="headline">Lorem Ipsum<br>Dolor Sit</h1>

  <section class="points">
    <div class="point-number" style="top:327.8px">01</div>
    <p class="point-text" style="top:324.7px">Lorem ipsum dolor sit amet, elit consectetuer adipiscing. Maecenas porttitor congue massa.</p>

    <div class="point-number" style="top:429px">02</div>
    <p class="point-text" style="top:425.8px">Lorem ipsum dolor sit amet, elit consectetuer adipiscing. Maecenas porttitor congue massa.</p>

    <div class="point-number" style="top:530px">03</div>
    <p class="point-text" style="top:527.3px">Lorem ipsum dolor sit amet, elit consectetuer adipiscing. Maecenas porttitor congue massa.</p>
  </section>
</main>
</body>
</html>
```